Simple and clean poster/flyer design needed for public speaker!

SIMPLE AND CLEAN DESIGN NEEDED FOR POSTER/FLYER

I AM a public speaker based in London (www.corvanlethby.com)
and I would like to have a custom-made flyer/poster
(preferably in adobe CS4 template format) that I con customize (just changing the text) for my various speeches, topics and locations

I am looking for something very simple and clean.
NO extravagance or crowded poster, but a rather beautiful clean and eye-catching design that clearly informs people what i am talking about, where and when.

Go to my website www.corvanlethby.com
to see the colour scheme and style that I like
my poster should be like the website, similar colours, logo, clean, simple and clear.

Summary

(1) simple and clean design
(2) design that fits my brand (see website)
(3) clear and eye-catching to promote my speeches
(4) customizable for my various talks, by simply chancing the text (Please Adobe Photoshop CS4 template format)
(5)in A3, A4, A5, A6 sizes, so i can use it for both flyers and small posters

ADDITIONS

BIG BOLD HEADLINE TO GRAP ATTENTION, greatest prominence

sub headline to explain, smaller than the headline, but still prominent on the poster

just a few bullet points to list the benefits and answer the “whats in for me”-question
this is for people who are already interested and continue reading, medium prominence.

WHERE, WHEN, HOW MUCH-information, in the lower section of the poster, little text, but clearly visible

only one point of CONTACT on my poster “www.corvanlethby.com”, bit big and clear so that it is very prominent

little text, effectively used
LESS IS MORE
Updates

contact me regarding logo files and any questions you may have!

for the logo files go to

https://share.dropvaultex.net/f/x.aspx?k=41c07d2e9ab35f18c6d2

click on the folder "logo pack" to see the files

thanks for your interest. hope to see great designs!
I am really looking forward to it
if you have any questions, please do not hesitate to ask

Kind Regards
Corvan
 

• Simple, clean design, text sparingly used.

• The mood should be light-hearted, calm, bright, simple and friendly, comic like

• a lot of white space, calling more attention to the content

• a light blue, dark blue, white and black colour scheme as seen on the homepage (www.corvanlethby.com) please use the exact same colours as seen on the homepage.

White being most predominant, 2 different blue used to highlight something, black for text on white background.

• One graphic would be cool, as long as it is blue. It could be waves-like graphic, or something like the white pattern in the background, in my case just in blue on white background > http://www.quillmereretreathouse.org/., I do not mean exactly this graphic and not that crowded but a simple single graphic in blue as long as it fits the theme and feel of my poster

Top o f the poster

• (a )One short bold headline (TALK TITLE) with a sub-headline below it (hook)

• or (b) headline as question (…....?) and below sub-headline offering the solution (my talk ;-) of course)

• 3 benefits as on homepage, that I can adapt for each talk (bottom right of my start site “what are you looking for?” either blue on white, or as in the page white on blue...whatever looks better and fits the design). Not sure how that looks, and if to include it!

• the bottom of the poster will have “Where”-information “when”-information “ticket price” info

• contact at the very bottom...for more into or to purchase tickets (my website and email)

If you have any questions or need clarification please write me!

Requirements
Must have
• lot of white space
• less is more - simple design
• little text, little graphics- only used when necessary to greatest effect.
• light, friendly, modern feel
• blue-color scheme

```html
<!DOCTYPE html>
<html lang="en">
<head>
<meta charset="utf-8">
<title>Is Life Happening To Me? — Talk Poster</title>
<link rel="stylesheet" href="https://fonts.googleapis.com/css2?family=Arimo:wght@400;700&display=swap">
<style>
  :root {
    --paper: #e6fbf9;
    --paper-top: #ecfdfc;
    --band-edge: #7fdedf;
    --band-core: #aaf1f0;
    --white: #ffffff;
    --bullet: #f1fdfc;
    --label: #70d4d7;
    --bubble: #eafcfb;
    --bubble-rim: #6fd3d6;
    --link: #18d8f0;
    --brand: #2bcfee;
  }
  * { margin: 0; padding: 0; box-sizing: border-box; }
  html, body { width: 849px; height: 1200px; overflow: hidden; }
  body { font-family: "Arimo", Arial, sans-serif; background: var(--paper); }

  .poster { position: relative; width: 849px; height: 1200px; background: var(--paper); overflow: hidden; }

  .masthead { position: absolute; left: 0; top: 0; width: 849px; height: 248px; background: var(--paper-top); }
  .brand { position: absolute; left: 0; top: 104px; width: 849px; display: flex; justify-content: center; align-items: center; gap: 12px; }
  .brand-dot { width: 18px; height: 18px; border-radius: 50%; background: var(--brand); }
  .brand-name { font-weight: 700; font-size: 34px; color: var(--brand); letter-spacing: 0.5px; }

  .feature-band {
    position: absolute; left: 0; top: 248px; width: 849px; height: 610px;
    background: radial-gradient(ellipse 60% 65% at 52% 40%, var(--band-core), var(--band-edge));
  }

  .headline { position: absolute; left: 89px; top: 291px; font-weight: 700; font-size: 51px; color: var(--white); white-space: nowrap; letter-spacing: -0.3px; }
  .headline-mark { position: absolute; left: 706px; top: 250px; font-weight: 400; font-size: 124px; line-height: 1; color: var(--white); }
  .subhead { position: absolute; right: 115px; top: 369px; font-weight: 700; font-size: 29px; color: var(--white); white-space: nowrap; }

  .benefits-title { position: absolute; left: 123px; top: 471px; font-weight: 700; font-size: 29px; color: var(--white); }
  .benefits { list-style: none; }
  .benefits li { position: absolute; left: 273px; width: 28px; height: 28px; border-radius: 50%; background: var(--bullet); }

  .details-bubble { position: absolute; left: 0; top: 740px; width: 849px; height: 220px; }

  .details { position: absolute; left: 0; top: 778px; width: 293px; text-align: right; font-size: 23px; line-height: 31px; color: var(--label); }

  .ornament-vine {
    position: absolute; left: 488px; top: 713px; width: 255px; height: 297px;
    background: linear-gradient(160deg, rgba(255,255,255,0.18), rgba(255,255,255,0.05));
    border-radius: 40px;
  }

  .contact-label { position: absolute; left: 0; top: 1001px; width: 849px; text-align: center; font-size: 22px; color: var(--label); }
  .contact-url { position: absolute; left: 0; top: 1037px; width: 849px; text-align: center; font-size: 60px; color: var(--link); letter-spacing: -0.5px; }
</style>
</head>
<body>
<main class="poster">
  <header class="masthead">
    <div class="brand"><span class="brand-dot"></span><span class="brand-name">Corvan Lethby</span></div>
  </header>

  <section class="feature-band"></section>

  <h1 class="headline">Is Life Happening To Me</h1>
  <span class="headline-mark" aria-hidden="true">?</span>
  <h2 class="subhead">A detail talk on meaning of life..</h2>

  <h3 class="benefits-title">what’s in for me?</h3>
  <ul class="benefits">
    <li style="top:528px"></li>
    <li style="top:591px"></li>
    <li style="top:656px"></li>
  </ul>

  <svg class="details-bubble" viewBox="0 740 849 220" width="849" height="220" aria-hidden="true">
    <path fill="var(--bubble-rim)" d="M62 762 H787 A60 60 0 0 1 847 822 V846 A60 60 0 0 1 787 906 H490 C455 906 440 930 425 956 C410 930 395 906 360 906 H62 A60 60 0 0 1 2 846 V822 A60 60 0 0 1 62 762 Z"/>
    <path fill="var(--bubble)" d="M62 757 H787 A60 60 0 0 1 847 817 V841 A60 60 0 0 1 787 901 H490 C455 901 440 925 425 950 C410 925 395 901 360 901 H62 A60 60 0 0 1 2 841 V817 A60 60 0 0 1 62 757 Z"/>
  </svg>

  <div class="ornament-vine" role="img" aria-label="Delicate white line-art vine with leaves curling over the details panel"></div>

  <dl class="details">
    <dt>where:</dt>
    <dt>when:</dt>
    <dt>get your ticket :</dt>
  </dl>

  <p class="contact-label">contact:</p>
  <p class="contact-url">www.corvanlethby.com</p>
</main>
</body>
</html>
```